Drug safety monitoring company requires a new corporate website

We are an outsourcing partner to large and small companies within the pharmaceutical industry. Our current website www.quorvanta.co.uk has not been updated in a long time. We want a new web site that is responsive and modern but with a clearly corporate and professional feel. We want a design based on a 12 column grid system (mobile and desktop version). We want to use a new, modern font (not the standard web fonts) - we will purchase as required. Content can be used as is from the current website. Red and white are the corporate colours, so a palate should be developed to match. We do not need as much red as is in the current website. New icons (preferably in svg format) would be great. We can also purchase new images from Framly (or other) as required. We would prefer submissions in Sketch if possible.

Target Market(s)

Pharmaceutical companies

Number of Pages Required

1 page

Font styles to use
Sans Serif

Colors
ec1f27
ffffff

Requirements
Must have
• Design based on 12 column grid system.
Responsive design (i.e. require a mobile and desktop version).
How should the menu look between desktop and mobile?
A coherent colour palete.
Content to come from the existing website: www.quorvanta.co.uk
How should links be styled?
How should headings, sub-headings, paragraphs be styled?
Nice to have
• Custom developed icons (these are along the bottom of the page on the existing website: Medical Information; Pharmacovigilance; Literature Monitoring; Training).
New imagery (the images on the current website are dated).
Submission ideally as Sketch files (but we are okay with photoshop too).
A new, modern, non-standard font.
Not so much red in the design.
If we had buttons on the website, how should they be styled?
If we had a form on the website, how should the fields be styled?

```html
<!DOCTYPE html>
<html lang="en">
<head>
<meta charset="utf-8">
<title>Quorvanta – Website Info Presentation</title>
<link href="https://fonts.googleapis.com/css2?family=Plus+Jakarta+Sans:wght@400;500;600;700;800&family=Allura&display=swap" rel="stylesheet">
<style>
:root{
  --red:#ec1f27;
  --white:#ffffff;
  --ink:#111114;
  --text:#2b2b2f;
  --muted:#55555c;
  --dark:#2a2a2e;
  --line:#e6e6e9;
  --script:#1aa3e8;
}
*{box-sizing:border-box;margin:0;padding:0}
html,body{width:1200px;height:3529px;overflow:hidden;background:var(--white)}
body{position:relative;font-family:"Plus Jakarta Sans",Arial,sans-serif;color:var(--ink)}
.section-title{position:absolute;left:0;width:1200px;text-align:center;font-weight:800;font-size:40px;letter-spacing:-.2px}

/* ---------- desktop page ---------- */
.desktop{position:absolute;width:1016px;overflow:hidden;background:var(--dark);transform-origin:0 0}
.site-header{position:absolute;left:0;top:0;width:100%;height:85px;background:var(--white);display:flex;align-items:center;padding:0 0 0 96px}
.brand{display:flex;align-items:center;gap:8px;font-weight:700;color:var(--red);letter-spacing:2px;font-size:17px}
.brand-dot{width:12px;height:12px;border-radius:50%;background:var(--red)}
.main-nav{display:flex;gap:17px;margin-left:103px;font-size:12.5px;font-weight:500;color:var(--text)}
.main-nav .active{border-bottom:2px solid var(--red);padding-bottom:4px}
.call{display:flex;align-items:center;gap:10px;margin-left:32px}
.call-label{font-size:10.5px;letter-spacing:2px;font-weight:600;color:var(--text)}
.call-number{font-size:16px;font-weight:700;color:var(--red)}
.hero-photo{position:absolute;right:0;top:85px;bottom:0;width:58%;
  background:radial-gradient(circle at 75% 20%,#e9e6e0 0,#c9c2ba 14%,transparent 34%),
  radial-gradient(circle at 45% 55%,#d9534f 0,#b64a48 10%,transparent 30%),
  radial-gradient(circle at 70% 70%,#ece8df 0,#bdb6ad 18%,transparent 40%),
  radial-gradient(circle at 30% 85%,#d8cf7a 0,transparent 18%),
  linear-gradient(120deg,var(--dark) 0,#4a4446 45%,#6d5e5f 100%)}
.hero-copy{position:absolute;left:99px;top:218px;color:var(--white)}
.hero-copy h1{font-size:32px;line-height:1.28;font-weight:700}
.hero-copy h1 .mark{border-bottom:2px solid var(--red)}
.hero-copy p{margin-top:16px;font-size:20px;line-height:1.3;font-weight:400}
.btn{display:inline-flex;align-items:center;justify-content:center;background:var(--red);color:var(--white);font-weight:700;border-radius:999px;text-transform:uppercase}
.hero-copy .btn{margin-top:26px;width:127px;height:42px;font-size:12px}
.dropdown{position:absolute;left:446px;top:87px;width:187px;background:var(--white);padding:4px 14px}
.dropdown li{list-style:none;font-size:11.5px;font-weight:500;color:var(--text);height:34px;display:flex;align-items:center;border-bottom:1px solid var(--line)}
.dropdown li:last-child{border-bottom:0}

/* ---------- phone page ---------- */
.phone{position:absolute;left:920px;top:310px;width:170px;height:371px;border-radius:14px;overflow:hidden;background:var(--dark);box-shadow:0 6px 20px rgba(0,0,0,.15)}
.phone-header{height:34px;background:var(--white);display:flex;align-items:center;justify-content:space-between;padding:0 10px}
.phone-header .brand{font-size:7px;gap:4px;letter-spacing:1px}
.phone-header .brand-dot{width:6px;height:6px}
.phone-copy{text-align:center;color:var(--white);padding:30px 8px 0}
.phone-copy h2{font-size:12px;line-height:1.35;font-weight:700}
.phone-copy p{font-size:7px;margin-top:4px;line-height:1.35}
.phone-copy .btn{margin-top:8px;width:54px;height:15px;font-size:5px}
.phone-photo{position:absolute;left:0;right:0;top:170px;height:160px;
  background:radial-gradient(circle at 40% 45%,#ece8df 0,#b8b0a6 22%,transparent 50%),radial-gradient(circle at 70% 65%,#d9534f 0,transparent 30%),linear-gradient(160deg,#2e2c2f,#5b5052)}
.phone-welcome{position:absolute;left:0;right:0;bottom:0;height:41px;background:var(--white);text-align:center;font-weight:700;font-size:15px;padding-top:12px}

/* ---------- mobile menu screens ---------- */
.mobile{position:absolute;top:1726px;width:339px;height:621px;overflow:hidden;background:var(--dark);box-shadow:0 4px 14px rgba(0,0,0,.12)}
.mobile-header{position:absolute;left:0;top:0;width:100%;height:56px;background:var(--white);display:flex;align-items:center;justify-content:space-between;padding:0 20px}
.mobile-header .brand{font-size:11px;gap:6px;letter-spacing:1.5px}
.mobile-header .brand-dot{width:8px;height:8px}
.burger{width:16px;height:13px;display:flex;flex-direction:column;justify-content:space-between}
.burger span{height:2.5px;background:var(--ink)}
.mobile-copy{position:absolute;left:0;right:0;top:70px;text-align:center;color:var(--white)}
.mobile-copy h2{font-size:27px;line-height:1.35;font-weight:700}
.mobile-copy p{font-size:17px;margin-top:10px;line-height:1.3}
.mobile-copy .btn{margin-top:16px;width:130px;height:32px;font-size:11px}
.mobile-photo{position:absolute;left:0;right:0;top:290px;bottom:0;
  background:radial-gradient(circle at 50% 45%,#ece8df 0,#b8b0a6 25%,transparent 55%),radial-gradient(circle at 25% 30%,#d8cf7a 0,transparent 18%),radial-gradient(circle at 80% 70%,#d9534f 0,transparent 25%),linear-gradient(160deg,#2e2c2f,#5b5052)}
.mobile-dim{position:absolute;left:0;right:0;top:56px;bottom:0;background:rgba(25,25,28,.5)}
.mobile-nav{position:absolute;left:194px;top:58px;width:134px;background:var(--white);padding:4px 12px}
.mobile-nav li,.mobile-sub li{list-style:none;font-size:11px;font-weight:500;color:var(--text);border-bottom:1px solid var(--line);display:flex;align-items:center}
.mobile-nav li{height:38px}
.mobile-nav li:last-child,.mobile-sub li:last-child{border-bottom:0}
.mobile-sub{position:absolute;left:14px;top:171px;width:167px;background:var(--white);padding:2px 10px}
.mobile-sub li{height:30px;font-size:10px}

/* ---------- buttons & cards ---------- */
.cta{position:absolute;top:2603px;width:207px;height:69px;font-size:20px}
.cta.is-hover{box-shadow:0 0 18px rgba(236,31,39,.55)}
.card{position:absolute;top:2773px;width:265px;height:253px;background:var(--white);box-shadow:0 2px 14px rgba(0,0,0,.1);text-align:center;padding-top:20px}
.card-icon{width:97px;height:97px;border-radius:50%;background:var(--red);margin:0 auto;display:flex;align-items:center;justify-content:center}
.card h3{font-size:21px;font-weight:700;margin-top:14px}
.card p{font-size:14.5px;line-height:1.6;color:var(--text);margin-top:8px;padding:0 14px}

.thanks{position:absolute;left:0;width:1200px;top:3150px;text-align:center;font-family:"Allura",cursive;font-size:130px;color:var(--script)}
</style>
</head>
<body>

<h2 class="section-title" style="top:46px">Website Info Presentation</h2>

<!-- desktop preview -->
<div class="desktop" style="left:190px;top:182px;height:637px;transform:scale(.683)">
  <header class="site-header">
    <div class="brand"><span class="brand-dot"></span>QUORVANTA</div>
    <nav class="main-nav"><span>HOME</span><span>ABOUT US</span><span>QPPV</span><span>OUR SERVICES</span><span>CONTACT US</span><span>CLIENT</span></nav>
    <div class="call">
      <svg width="30" height="30" viewBox="0 0 24 24"><path fill="#ec1f27" d="M6.6 10.8a15.1 15.1 0 0 0 6.6 6.6l2.2-2.2c.3-.3.7-.4 1-.2 1.1.4 2.3.6 3.6.6.6 0 1 .4 1 1V20c0 .6-.4 1-1 1A17 17 0 0 1 3 4c0-.6.4-1 1-1h3.5c.6 0 1 .4 1 1 0 1.3.2 2.5.6 3.6.1.3 0 .7-.2 1z"/></svg>
      <div><div class="call-label">CALL US TODAY!</div><div class="call-number">0330 4820 175</div></div>
    </div>
  </header>
  <div class="hero-photo" role="img" aria-label="Photo of colourful pills spilling from a white bottle on a dark surface"></div>
  <div class="hero-copy" style="top:180px">
    <h1>At <span class="mark">Quorvanta</span> We Ensure<br>That Your Business</h1>
    <p>has the best Pharmacovigilance<br>support in the industry</p>
    <span class="btn">Contact us</span>
  </div>
</div>

<!-- phone preview -->
<div class="phone">
  <div class="phone-header"><div class="brand"><span class="brand-dot"></span>QUORVANTA</div><div class="burger" style="width:8px;height:7px"><span style="height:1.5px"></span><span style="height:1.5px"></span><span style="height:1.5px"></span></div></div>
  <div class="phone-copy">
    <h2>At Quorvanta We Ensure<br>That Your Business</h2>
    <p>has the best Pharmacovigilance<br>support in the industry</p>
    <span class="btn">Contact us</span>
  </div>
  <div class="phone-photo" role="img" aria-label="Photo of pills spilling from a bottle"></div>
  <div class="phone-welcome">Welcome to</div>
</div>

<h2 class="section-title" style="top:830px">Desktop Menu :</h2>

<div class="desktop" style="left:92px;top:912px;height:579px">
  <header class="site-header">
    <div class="brand"><span class="brand-dot"></span>QUORVANTA</div>
    <nav class="main-nav"><span>HOME</span><span>ABOUT US</span><span>QPPV</span><span class="active">OUR SERVICES</span><span>CONTACT US</span><span>CLIENT</span></nav>
    <div class="call">
      <svg width="30" height="30" viewBox="0 0 24 24"><path fill="#ec1f27" d="M6.6 10.8a15.1 15.1 0 0 0 6.6 6.6l2.2-2.2c.3-.3.7-.4 1-.2 1.1.4 2.3.6 3.6.6.6 0 1 .4 1 1V20c0 .6-.4 1-1 1A17 17 0 0 1 3 4c0-.6.4-1 1-1h3.5c.6 0 1 .4 1 1 0 1.3.2 2.5.6 3.6.1.3 0 .7-.2 1z"/></svg>
      <div><div class="call-label">CALL US TODAY!</div><div class="call-number">0330 4820 175</div></div>
    </div>
  </header>
  <div class="hero-photo" role="img" aria-label="Photo of colourful pills spilling from a white bottle on a dark surface"></div>
  <div class="hero-copy">
    <h1>At <span class="mark">Quorvanta</span> We Ensure<br>That Your Business</h1>
    <p>has the best Pharmacovigilance<br>support in the industry</p>
    <span class="btn">Contact us</span>
  </div>
  <ul class="dropdown">
    <li>MEDICAL INFORMATION</li><li>PHARMACOVIGILANCE</li><li>LITERATURE MONITORING</li><li>TRAINING</li>
  </ul>
</div>

<h2 class="section-title" style="top:1592px">Mobile Menu :</h2>

<div class="mobile" style="left:216px">
  <div class="mobile-header"><div class="brand"><span class="brand-dot"></span>QUORVANTA</div><div class="burger"><span></span><span></span><span></span></div></div>
  <div class="mobile-photo" role="img" aria-label="Photo of pills spilling from a bottle"></div>
  <div class="mobile-copy"><h2>At Quorvanta We Ensure<br>That Your Business</h2><p>has the best Pharmacovigilance<br>support in the industry</p><span class="btn">Contact us</span></div>
  <div class="mobile-dim"></div>
  <ul class="mobile-nav"><li>HOME</li><li>ABOUT US</li><li>QPPV</li><li>OUR SERVICES</li><li>CONTACT US</li><li>CLIENT</li></ul>
</div>

<div class="mobile" style="left:623px">
  <div class="mobile-header"><div class="brand"><span class="brand-dot"></span>QUORVANTA</div><div class="burger"><span></span><span></span><span></span></div></div>
  <div class="mobile-photo" role="img" aria-label="Photo of pills spilling from a bottle"></div>
  <div class="mobile-copy"><h2>At Quorvanta We Ensure<br>That Your Business</h2><p>has the best Pharmacovigilance<br>support in the industry</p><span class="btn">Contact us</span></div>
  <div class="mobile-dim"></div>
  <ul class="mobile-nav"><li>HOME</li><li>ABOUT US</li><li>QPPV</li><li>OUR SERVICES</li><li>CONTACT US</li><li>CLIENT</li></ul>
  <ul class="mobile-sub"><li>MEDICAL INFORMATION</li><li>PHARMACOVIGILANCE</li><li>LITERATURE MONITORING</li><li>TRAINING</li></ul>
</div>

<h2 class="section-title" style="top:2505px">Button And Icon Design :</h2>

<span class="btn cta" style="left:371px">Contact us</span>
<span class="btn cta is-hover" style="left:608px">Contact us</span>

<div class="card" style="left:284px">
  <div class="card-icon">
    <svg width="48" height="48" viewBox="0 0 48 48" fill="none" stroke="#fff" stroke-width="2"><rect x="14" y="6" width="24" height="30" rx="2"/><rect x="9" y="12" width="24" height="30" rx="2" fill="#ec1f27"/><circle cx="21" cy="22" r="5"/><path d="M21 19v6M18 22h6M14 31h14M14 35h14M14 39h9"/></svg>
  </div>
  <h3>Medical Information</h3>
  <p>Professional enquiry handling to support the safe and effective use of your products</p>
</div>

<div class="card" style="left:616px">
  <div class="card-icon">
    <svg width="48" height="48" viewBox="0 0 48 48" fill="none" stroke="#fff" stroke-width="2"><rect x="14" y="6" width="24" height="30" rx="2"/><rect x="9" y="12" width="24" height="30" rx="2" fill="#ec1f27"/><circle cx="21" cy="22" r="5"/><path d="M21 19v6M18 22h6M14 31h14M14 35h14M14 39h9"/></svg>
  </div>
  <h3>Medical Information</h3>
  <p>Professional enquiry handling to support the safe and effective use of your products</p>
</div>

<div class="thanks">Thanks For Watching!</div>

</body>
</html>
```